Website Design for a Luxury Wedding & Events Company

We are launching a British luxury wedding & event planning consultancy business providing bespoke, elegant and first-class service to our discerning clients in the UK and abroad. We specialize in Weddings (which will have it's on page) however we also provide service for other occasion which will be included in a single page 'Events'.

We require a company website design befitting of our luxury brand. Once designed we will post another job to code the website so that it can be hosted by HostQuill.com.

The website has to set the tone for our business and type of premium service we provide. Our website design has to be BESPOKE and have a luxury and elegant look and feel about it.

PLEASE REFER TO THE IMAGES ATTACHED TO GET AN UNDERSTANDING OF THE DESIGN CONCEPT WE WANT. ALL DESIGNS SUBMITTED MUST FOLLOW THE CONCEPT SPECIFIED!!!

We appreciate that the current budget will not permit for the design of all pages referenced above, so we are happy to have designs for up to 3 pages initially; Landing page (we have attached an examples of what we want), 'Home' page (an example is also attached) and 'About' us page. When we are happy with a particular design we can add payment for remainder of the pages required.

The final website design will have the following pages:
1a) URL Landing Page (details below)
1b) Home
2) About
3) Luxury Weddings
4) Services (this can either be a separate tab or linked to 'Luxury Weddings' - however it does need to be a separate page)
subheadings are:
> Comprehensive Wedding Planning Service
> Wedding Day Coordination Service
> Consultancy Service
5) Events
6) Gallery
7) Testimonials
8) Contact

We have a concept of the website is as follows:
URL Landing Page:
Option 1: This should just be simple but makes an immediate statement.
We have attached an image of how this could potentially look. The logo featured in the photo example needs to be replaced with our logo (reference site: http://tessawirth.com/).

Option 2: Alternatively this could be an actually door in the middle of the page - Imagine the big black gloss door at Number 7 Fenwick Terrace (London Prime Minister's home).

By clicking the door knocker on either options , the 'Home Page' will be opened.

Our tag line should also be tastefully integrated:
'Exclusive Events, Masterfully Produced, Distinctively Designed'

The 'HOME PAGE' - should look like a luxury boutique office or reception lounge (luxury table, luxury head chair and luxury 2 client chairs; elegant chandelier, beautiful flowers on the table, 2 flutes of champagne on the table; and filing cabinets with drawers that are labelled with different website pages, e.g. 'about us', 'services', 'gallery', etc. By clicking on the drawers the details behind that page will open up in a separate tab/page.)

Our tag line should be on the Home Page also.

The overall concept and look and feel of website is all about taking people on a journey and giving them a glimpse of the luxury service that awaits them.

Colours: We want the general look and feel of the website to be WHITE, or OFF-WHITE with soft hints of gold to match the logo (tab/page headings could be gold). The only dark page should be the URL Landing page (ref to website images attached).

The website and images need to be compatible with mobile devices, smartphones, iPads, etc. In terms of fit to screen, resolution etc...

We require links to our Facebook, Twitter, Instagram and Pinterest Pages (links to be provided later)

This is the rough concept and looking for designers to try to elevate this vision. :-) We are open for designers to interpret this concept in their own way.

Website wording/content is all ready to go...

We have attached our logo, and some imagery to help...

Target Market(s)

Luxury Wedding & Events Market

Industry/Entity Type

Wedding Planner

Number of Pages Required

3 page

Font styles to use
Sans Serif

Colors
ffffff

Requirements
Must have
• Tag Line:
• 'Exquisite Events, Masterfully Produced, Distinctively Designed'

```html
<!DOCTYPE html>
<html lang="en">
<head>
<meta charset="utf-8">
<title>Elena Marlowe — Luxury Wedding &amp; Event Consultants</title>
<link rel="stylesheet" href="https://fonts.googleapis.com/css2?family=Maven+Pro:wght@500&family=PT+Sans:wght@400&display=swap">
<style>
  :root {
    --ink: #111111;
    --ink-rule: #3a3a3a;
    --gold: #c5954a;
    --gold-light: #f6d27e;
    --gold-text: #d9b25f;
    --cream: #f4f0ea;
    --nav-text: #f2f2f2;
    --caption-bg: rgba(244, 242, 240, 0.72);
    --caption-text: #151515;
    --foot-text: #cfcfcf;
  }
  * { box-sizing: border-box; margin: 0; padding: 0; }
  html, body { width: 1200px; height: 985px; overflow: hidden; background: var(--cream); }
  body { font-family: "PT Sans", sans-serif; position: relative; }

  .site-header { position: absolute; top: 0; left: 0; width: 1200px; height: 137px; background: var(--ink); }
  .brand { position: absolute; top: 20px; left: 0; width: 1200px; text-align: center; color: var(--gold-text); }
  .brand-mark { display: block; width: 60px; height: 60px; margin: 0 auto; border-radius: 50%; border: 2px solid var(--gold-text); }
  .brand-name { display: block; margin-top: 10px; font-family: "PT Sans", sans-serif; font-size: 18px; letter-spacing: 2.5px; line-height: 1; }
  .brand-tag { display: block; margin-top: 3px; font-size: 7px; letter-spacing: 0.6px; line-height: 1; }

  .main-nav { position: absolute; top: 137px; left: 0; width: 1200px; height: 53px; background: var(--ink); border-top: 2px dotted var(--ink-rule); }
  .main-nav ul { list-style: none; display: flex; justify-content: center; align-items: center; height: 51px; }
  .main-nav li { display: flex; align-items: center; color: var(--nav-text); font-size: 13px; letter-spacing: 0.2px; }
  .main-nav li.current { color: var(--gold-light); }
  .nav-sep { width: 7px; height: 7px; margin: 0 28px; transform: rotate(45deg); border: 1px solid var(--gold); }

  .hero { position: absolute; top: 212px; left: 111px; width: 990px; height: 542px; overflow: hidden;
    background:
      radial-gradient(ellipse at 80% 25%, #f6f2e6 0%, rgba(246,242,230,0) 40%),
      radial-gradient(ellipse at 55% 30%, #e7c3c2 0%, rgba(231,195,194,0) 35%),
      radial-gradient(ellipse at 88% 60%, #2a2a26 0%, rgba(42,42,38,0) 22%),
      radial-gradient(ellipse at 10% 20%, #f3ece3 0%, rgba(243,236,227,0) 45%),
      linear-gradient(180deg, #e9ddd0 0%, #d8cbbd 60%, #c9b9a8 100%); }
  .slider-arrow { position: absolute; top: 480px; width: 38px; height: 38px; }
  .slider-arrow.prev { left: 138px; }
  .slider-arrow.next { left: 1034px; }

  .hero-caption { position: absolute; top: 543px; left: 155px; width: 797px; height: 161px; background: var(--caption-bg); padding: 30px 0 0 53px; }
  .hero-caption h1 { font-family: "Maven Pro", sans-serif; font-weight: 500; font-size: 38px; line-height: 52px; color: var(--caption-text); letter-spacing: 0.3px; text-transform: uppercase; white-space: nowrap; }

  .social-band { position: absolute; top: 795px; left: 0; width: 1200px; height: 111px; background: var(--gold); display: flex; justify-content: center; align-items: center; gap: 9px; }
  .social-link { display: block; width: 43px; height: 43px; border-radius: 50%; background: var(--gold-light); }

  .site-footer { position: absolute; top: 906px; left: 0; width: 1200px; height: 79px; background: var(--ink); text-align: center; padding-top: 31px; font-size: 12.5px; color: var(--foot-text); }
  .site-footer .brand-ref { color: var(--gold-light); }
</style>
</head>
<body>
  <header class="site-header">
    <div class="brand">
      <span class="brand-mark"></span>
      <span class="brand-name">ELENA MARLOWE</span>
      <span class="brand-tag">LUXURY WEDDING &amp; EVENT CONSULTANTS</span>
    </div>
  </header>

  <nav class="main-nav">
    <ul>
      <li class="current">HOME</li><li><span class="nav-sep"></span></li>
      <li>ABOUT</li><li><span class="nav-sep"></span></li>
      <li>LUXURY WEDDINGS</li><li><span class="nav-sep"></span></li>
      <li>SERVICES</li><li><span class="nav-sep"></span></li>
      <li>EVENTS</li><li><span class="nav-sep"></span></li>
      <li>GALLERY</li><li><span class="nav-sep"></span></li>
      <li>TESTIMONIALS</li><li><span class="nav-sep"></span></li>
      <li>CONTACT</li>
    </ul>
  </nav>

  <div class="hero" role="img" aria-label="Photograph of a wedding table setting with crystal glasses, a candle, pink and white roses and a chalkboard table number"></div>

  <svg class="slider-arrow prev" viewBox="0 0 38 38" aria-label="Previous slide">
    <circle cx="19" cy="19" r="16" fill="rgba(255,255,255,0.35)" stroke="#c8c8c8" stroke-width="3"/>
    <path d="M22 11 L13 19 L22 27 Z" fill="#b5b5b5"/>
  </svg>
  <svg class="slider-arrow next" viewBox="0 0 38 38" aria-label="Next slide">
    <circle cx="19" cy="19" r="16" fill="rgba(255,255,255,0.35)" stroke="#c8c8c8" stroke-width="3"/>
    <path d="M16 11 L25 19 L16 27 Z" fill="#b5b5b5"/>
  </svg>

  <div class="hero-caption">
    <h1>Exclusive Events, Masterfully<br>Produced, Distinctively Designed</h1>
  </div>

  <section class="social-band">
    <a class="social-link" aria-label="Social profile one"></a>
    <a class="social-link" aria-label="Social profile two"></a>
    <a class="social-link" aria-label="Social profile three"></a>
    <a class="social-link" aria-label="Social profile four"></a>
  </section>

  <footer class="site-footer">
    Copyrights @ 2015 <span class="brand-ref">Elena Marlowe.</span> All Rights Reserved.
  </footer>
</body>
</html>
```